Business card design needed

We would like a new design for our window furnishings & home decor business. We supply & install blinds, curtains, shutters etc. We are about to incorporate home decor products like cushoins & throws...
We'd like to use moderns browns & green tones. Casual but elegant style. Maybe textured/patterned look design. Design should communicate quality and great value with latest designs.

website & FB page & email is still to be advised so pls provide space.

Industry/Entity Type

Business

Contact Information for Business Card

Marlowe Haven
Window Furnishings & Home Decor
Genevieve - Interior Stylist
Call us now for a free measure & quote - 63124089
0412 906 358
0418 273 564

```html
<!DOCTYPE html>
<html lang="en">
<head>
<meta charset="utf-8">
<title>Marlowe Haven – Business Card</title>
<link rel="stylesheet" href="https://fonts.googleapis.com/css2?family=Crimson+Text:wght@400&display=swap">
<style>
  :root {
    --wood-light: #6e2f22;
    --wood-mid: #4a1d14;
    --wood-dark: #241009;
    --ink: #f4ece6;
    --ornament: #efe6df;
  }
  html, body {
    margin: 0;
    padding: 0;
    width: 1200px;
    height: 691px;
    overflow: hidden;
    background: var(--wood-dark);
  }
  .card {
    position: relative;
    width: 1200px;
    height: 691px;
    overflow: hidden;
    font-family: "Crimson Text", Georgia, serif;
    color: var(--ink);
    background:
      radial-gradient(ellipse 70% 75% at 50% 42%, var(--wood-light) 0%, var(--wood-mid) 55%, var(--wood-dark) 100%);
  }
  .brand {
    position: absolute;
    left: 54px;
    top: 44px;
  }
  .brand-name {
    margin: 0;
    font-size: 52px;
    font-weight: 400;
    line-height: 1;
    letter-spacing: 1px;
    color: var(--ink);
  }
  .brand-rule {
    width: 355px;
    height: 3px;
    margin-top: 10px;
    background: var(--ink);
  }
  .brand-tagline {
    margin: 6px 0 0;
    font-size: 14px;
    line-height: 1.2;
    color: var(--ink);
  }
  .ornament {
    position: absolute;
    left: 577px;
    top: 209px;
    width: 48px;
    height: 330px;
  }
  .contact {
    position: absolute;
    left: 671px;
    top: 222px;
    font-size: 23.5px;
    line-height: 33.6px;
    margin: 0;
  }
  .contact p {
    margin: 0;
  }
  .contact .intro {
    margin-bottom: 33.6px;
    width: 400px;
  }
</style>
</head>
<body>
  <div class="card">
    <header class="brand">
      <h1 class="brand-name">Marlowe Haven</h1>
      <div class="brand-rule"></div>
      <p class="brand-tagline">Window Furnishings &amp; Home Decor Genevieve</p>
    </header>

    <svg class="ornament" viewBox="0 0 48 330" role="img" aria-label="Decorative white scroll bracket ornament">
      <rect x="0" y="0" width="48" height="330" rx="20" fill="var(--ornament)" opacity="0.85"/>
    </svg>

    <section class="contact">
      <p class="intro">Interior Stylist Call us now for a free measure &amp; quote</p>
      <p class="phone">63124089</p>
      <p class="phone">0412 906 358</p>
      <p class="phone">0418 273 564</p>
      <p class="email">Yourname@marlowehaven.com</p>
      <p class="web">www.marlowehaven.com</p>
      <p class="social">social.page/marlowehaven</p>
    </section>
  </div>
</body>
</html>
```